Dance Card to Provide Contact Info

I'm looking for a double sided business card to provide contact information to perspective dance partners.
One side of the card would have the words: "Yes I would love to Dance" written in an interesting and eye catching way. Below that would be the three categories I'm interested in
>Social >Exhibition >Competition
The other side of the card would include a picture of me with my Name, Phone Number, and Email Address (Dale Pruitt, 210-574-1328, dale@twirlnstep.dance)
My target market is middle aged women interested in Country and Western dancing and West Coast Swing dancing. I am NOT particularly interested in Ballroom style.
Here are a few links to the type of dancing I want to do:
http://www.plvkrn.org/
http://www.prairiefolkstepsociety.com/
http://mesquitevalleytwostep.com/
Dale Pruitt
210-574-1328
dale@twirlnstep.dance

```html
<!DOCTYPE html>
<html lang="en">
<head>
<meta charset="utf-8">
<title>Dale Pruitt – Dance Card</title>
<link rel="stylesheet" href="https://fonts.googleapis.com/css2?family=Open+Sans:wght@400;600&family=Raleway:wght@300&display=swap">
<style>
  :root {
    --page: #e9e7e5;
    --card-light: #f2efee;
    --card-dark: #080808;
    --ink-dark: #111111;
    --ink-light: #ffffff;
    --ink-soft: #e4e4e4;
    --portrait-top: #d9a182;
    --portrait-mid: #b57352;
    --portrait-low: #141414;
  }
  html, body {
    margin: 0;
    width: 1200px;
    height: 900px;
    overflow: hidden;
    background: var(--page);
  }
  .canvas {
    position: relative;
    width: 1200px;
    height: 900px;
  }
  .card {
    position: absolute;
    width: 556px;
    height: 343px;
    overflow: hidden;
    background: var(--card-dark);
    box-shadow: 0 6px 18px rgba(0,0,0,0.18);
  }
  .card__band-light {
    position: absolute;
    left: 0; top: 0; right: 0;
    height: 124px;
    background: var(--card-light);
  }
  .card__portrait {
    position: absolute;
    top: 0;
    height: 343px;
    width: 262px;
    background: linear-gradient(180deg, var(--portrait-top) 0%, var(--portrait-mid) 45%, var(--portrait-low) 62%, var(--portrait-low) 100%);
  }

  /* Contact side */
  .card--contact { left: 238px; top: 62px; }
  .card--contact .card__portrait { right: 0; }
  .contact__name {
    position: absolute;
    left: 32px; top: 36px;
    margin: 0;
    font-family: "Open Sans", sans-serif;
    font-weight: 600;
    font-size: 43px;
    letter-spacing: 0.3px;
    color: var(--ink-dark);
  }
  .contact__list {
    position: absolute;
    left: 32px; top: 200px;
    margin: 0; padding: 0;
    list-style: none;
    font-family: "Open Sans", sans-serif;
    font-size: 18px;
    color: var(--ink-light);
  }
  .contact__item {
    display: flex;
    align-items: center;
    height: 27px;
  }
  .contact__icon {
    width: 13px; height: 13px;
    margin-right: 14px;
    fill: var(--ink-light);
  }

  /* Invitation side */
  .card--invite { left: 458px; top: 518px; width: 560px; }
  .card--invite .card__portrait { left: 0; width: 256px; }
  .invite__tagline {
    position: absolute;
    right: 39px; top: 142px;
    margin: 0;
    text-align: right;
    font-family: "Raleway", sans-serif;
    font-weight: 300;
    font-size: 32px;
    line-height: 42px;
    color: var(--ink-soft);
  }
  .invite__styles {
    position: absolute;
    right: 39px; top: 246px;
    margin: 0; padding: 0;
    list-style: none;
    text-align: right;
    font-family: "Open Sans", sans-serif;
    font-size: 18px;
    line-height: 25.5px;
    color: var(--ink-light);
  }
  .invite__arrow {
    display: inline-block;
    margin-left: 6px;
    font-size: 12px;
  }
</style>
</head>
<body>
<main class="canvas">

  <section class="card card--contact">
    <div class="card__band-light"></div>
    <h1 class="contact__name">Dale Pruitt</h1>
    <ul class="contact__list">
      <li class="contact__item">
        <svg class="contact__icon" viewBox="0 0 24 24" aria-hidden="true"><path d="M6.6 10.8c1.4 2.8 3.8 5.1 6.6 6.6l2.2-2.2c.3-.3.7-.4 1-.2 1.1.4 2.3.6 3.6.6.6 0 1 .4 1 1V20c0 .6-.4 1-1 1C10.6 21 3 13.4 3 4c0-.6.4-1 1-1h3.5c.6 0 1 .4 1 1 0 1.3.2 2.5.6 3.6.1.3 0 .7-.2 1z"/></svg>
        <span>210-574-1328</span>
      </li>
      <li class="contact__item">
        <svg class="contact__icon" viewBox="0 0 24 24" aria-hidden="true"><path d="M2 5h20v14H2z M3.5 6.5 12 13l8.5-6.5" stroke="#080808" stroke-width="1.6"/></svg>
        <span>dale@twirlnstep.dance</span>
      </li>
    </ul>
    <div class="card__portrait" role="img" aria-label="Portrait photo of Dale Pruitt in a black shirt"></div>
  </section>

  <section class="card card--invite">
    <div class="card__band-light"></div>
    <div class="card__portrait" role="img" aria-label="Portrait photo of Dale Pruitt smiling, wearing a black shirt"></div>
    <p class="invite__tagline">Yes I would love<br>to Dance</p>
    <ul class="invite__styles">
      <li>Social<span class="invite__arrow">◄</span></li>
      <li>Exhibition<span class="invite__arrow">◄</span></li>
      <li>Competition<span class="invite__arrow">◄</span></li>
    </ul>
  </section>

</main>
</body>
</html>
```